American cannabis tech company business card design

Thrum.com is seeking a modern, professional, and brand-aligned business card that represents our company and its core values: Mission, Story, Values, and Impact. As an innovative cannabis company, we want a business card that is not only visually appealing but also serves as a representation of who we are and what we stand for.

Project Scope: Design a double-sided business card that integrates our brand identity and core values. Incorporate our key brand elements, ensuring a sleek and contemporary aesthetic. Visually reflect our core values (Mission, Story, Values, Impact) in a way that is engaging yet professional.

Target Market(s)

Vendors, third parties,

Contact Information for Business Card

Contact details (name, title, email, phone, website, etc.)

Font styles to use
Other font styles liked:
• Caslon, Centra

Colors

Designer to choose colors to be used in the design.

Requirements
Must have
• Thrum.com logo and branding A creative yet clean way to integrate our core values (Mission, Story, Values, Impact) Modern typography and a well-structured layout
Nice to have
• forest green, grey, white, black
Should not have
• references to marijuana, leafs, plants, or related product

```html
<!DOCTYPE html>
<html lang="en">
<head>
<meta charset="utf-8">
<title>Thrum.com Business Card</title>
<link rel="stylesheet" href="https://fonts.googleapis.com/css2?family=Montserrat:wght@400;700;800&display=swap">
<style>
  :root {
    --backdrop: #3a3a3a;
    --forest: #1b3a1e;
    --forest-deep: #1a341c;
    --forest-mid: #2a5a31;
    --paper: #ffffff;
    --ink: #1b2a1c;
  }
  * { margin: 0; padding: 0; box-sizing: border-box; }
  html, body { width: 1200px; height: 689px; overflow: hidden; }
  body {
    background: var(--backdrop);
    font-family: "Montserrat", sans-serif;
    position: relative;
  }
  .card {
    position: absolute;
    top: 196px;
    width: 520px;
    height: 297px;
    border-radius: 22px;
    overflow: hidden;
  }
  .card--back {
    left: 50px;
    background: var(--forest);
    display: flex;
    align-items: center;
    justify-content: center;
  }
  .card--back .wordmark {
    font-weight: 800;
    font-size: 110px;
    letter-spacing: 2px;
    color: var(--forest-mid);
  }
  .card--front {
    left: 630px;
    background: var(--paper);
    display: flex;
    align-items: center;
    padding: 0 34px 0 44px;
  }
  .card--front .wordmark {
    font-weight: 800;
    font-size: 50px;
    color: var(--forest-deep);
    letter-spacing: 1px;
    width: 200px;
    margin-top: 60px;
  }
  .divider {
    width: 1.5px;
    height: 130px;
    background: var(--ink);
    margin: 0 22px 0 14px;
  }
  .contact { color: var(--ink); }
  .contact .name {
    font-weight: 800;
    font-size: 22px;
    letter-spacing: 0.5px;
    color: var(--forest-deep);
  }
  .contact .title {
    font-size: 13px;
    margin-top: 2px;
    margin-bottom: 16px;
  }
  .contact ul { list-style: none; }
  .contact li {
    display: flex;
    align-items: center;
    gap: 8px;
    font-size: 13px;
    line-height: 22px;
  }
  .contact svg { width: 11px; height: 11px; fill: var(--forest-deep); }
</style>
</head>
<body>
  <section class="card card--back" aria-label="Card back">
    <span class="wordmark">THRUM</span>
  </section>

  <section class="card card--front" aria-label="Card front">
    <span class="wordmark">THRUM</span>
    <span class="divider"></span>
    <div class="contact">
      <p class="name">DANIEL AVERY</p>
      <p class="title">Managing Director</p>
      <ul>
        <li>
          <svg viewBox="0 0 24 24" aria-hidden="true"><path d="M6.6 10.8a15 15 0 0 0 6.6 6.6l2.2-2.2a1 1 0 0 1 1-.25 11.4 11.4 0 0 0 3.6.57 1 1 0 0 1 1 1V20a1 1 0 0 1-1 1A17 17 0 0 1 3 4a1 1 0 0 1 1-1h3.5a1 1 0 0 1 1 1c0 1.25.2 2.45.57 3.6a1 1 0 0 1-.25 1z"/></svg>
          +1 405-555-0148
        </li>
        <li>
          <svg viewBox="0 0 24 24" aria-hidden="true"><path d="M2 5h20v14H2z M2 5l10 8 10-8" /><path d="M2 6l10 7.5L22 6v1.5l-10 7.5L2 7.5z" fill="#fff"/></svg>
          team@thrum.com
        </li>
        <li>
          <svg viewBox="0 0 24 24" aria-hidden="true"><circle cx="12" cy="12" r="10"/></svg>
          www.thrum.com
        </li>
      </ul>
    </div>
  </section>
</body>
</html>
```